Torvel, Inc. new buisness cards - brand guide included

We need new business cards. SLEAK SIMPLE FINANCE. They must include a place for NAME, TITLE, CELL, OFFICE PHONE, EMAIL. they also must include our services across the bottom. AIR, OCEAN, FTL, LTL, EXPRESS. for reference this will be being handed to some of the most prestigious shipping companies in a america.

Target Market(s)

Finance and corporate

Contact Information for Business Card

We need new business cards. SLEAK SIMPLE FINANCE. They must include a place for NAME, TITLE, CELL, OFFICE PHONE, EMAIL. they also must include our services across the bottom. AIR, OCEAN, FTL, LTL, EXPRESS.

Requirements
Must have
• We need new business cards. SLEAK SIMPLE FINANCE. They must include a place for NAME, TITLE, CELL, OFFICE PHONE, EMAIL. they also must include our services across the bottom. AIR, OCEAN, FTL, LTL, EXPRESS.
Nice to have
• USE THE COLORS AND LOGO IN THE BRAND GUIDE :)

```html
<!DOCTYPE html>
<html lang="en">
<head>
<meta charset="utf-8">
<title>Torvel, Inc. Business Cards</title>
<link rel="stylesheet" href="https://fonts.googleapis.com/css2?family=Tinos&display=swap">
<style>
  :root {
    --backdrop: #a4a2a3;
    --sand: #c4b698;
    --charcoal: #323232;
    --white: #ffffff;
  }
  * { margin: 0; padding: 0; box-sizing: border-box; }
  html, body {
    width: 1200px; height: 1200px; overflow: hidden;
    background: var(--backdrop);
    font-family: "Tinos", "Times New Roman", serif;
    color: var(--white);
  }
  .card {
    position: absolute; left: 275px; width: 650px; height: 371px;
    background: var(--sand); overflow: hidden;
  }
  .card--front { top: 208px; }
  .card--back { top: 620px; }
  .card__wave { position: absolute; left: 0; top: 0; width: 650px; height: 371px; }
  .front__brand {
    position: absolute; left: 0; right: 0; top: 150px;
    text-align: center; font-size: 62px; letter-spacing: 6px; line-height: 1;
  }
  .back__tagline {
    position: absolute; left: 47px; top: 46px;
    font-size: 38px; letter-spacing: 0.5px; line-height: 1; white-space: nowrap;
  }
  .contact-list { position: absolute; left: 48px; top: 106px; list-style: none; }
  .contact-list__item {
    display: flex; align-items: center; height: 24px;
    font-size: 24px; white-space: nowrap;
  }
  .contact-list__item + .contact-list__item { margin-top: 25px; }
  .contact-list__item:last-child { margin-top: 19px; }
  .contact-list__icon { width: 26px; height: 26px; margin-right: 12px; flex: none; }
  .back__services {
    position: absolute; left: 85px; top: 251px;
    font-size: 22px; white-space: nowrap; line-height: 1;
  }
  .back__badge {
    position: absolute; left: 503px; top: 79px; width: 190px; height: 190px;
    border-radius: 50%; background: var(--charcoal);
  }
  .back__badge-name {
    position: absolute; left: 0; width: 150px; top: 82px;
    text-align: center; font-size: 24px; letter-spacing: 2px; line-height: 1;
  }
</style>
</head>
<body>

<section class="card card--front">
  <div class="front__brand">TORVEL</div>
  <svg class="card__wave" viewBox="0 0 650 371" aria-hidden="true">
    <path fill="var(--white)" d="M0,308 C120,290 250,285 330,330 C420,375 560,330 650,292 L650,371 L0,371 Z"/>
    <path fill="var(--charcoal)" d="M0,332 C130,312 250,315 330,350 C420,385 560,355 650,318 L650,371 L0,371 Z"/>
  </svg>
</section>

<section class="card card--back">
  <h1 class="back__tagline">SLEAK SIMPLE FINANCE</h1>
  <ul class="contact-list">
    <li class="contact-list__item">
      <svg class="contact-list__icon" viewBox="0 0 26 26" aria-hidden="true">
        <circle cx="13" cy="13" r="12" fill="var(--white)"/>
        <rect x="9" y="6" width="8" height="14" rx="1.5" fill="var(--sand)"/>
        <rect x="10.5" y="8" width="5" height="9" fill="var(--white)"/>
      </svg>0123456789
    </li>
    <li class="contact-list__item">
      <svg class="contact-list__icon" viewBox="0 0 26 26" aria-hidden="true">
        <circle cx="13" cy="13" r="12" fill="var(--white)"/>
        <path fill="var(--sand)" d="M8,6.5 L10.5,6 L12,9.5 L10.5,11 C11.3,13 13,14.7 15,15.5 L16.5,14 L20,15.5 L19.5,18 C18.8,19.2 17,19.6 15,18.8 C11.5,17.3 8.7,14.5 7.2,11 C6.4,9 6.8,7.2 8,6.5 Z"/>
      </svg>310-555-0147
    </li>
    <li class="contact-list__item">
      <svg class="contact-list__icon" viewBox="0 0 26 26" aria-hidden="true">
        <circle cx="13" cy="13" r="12" fill="var(--white)"/>
        <rect x="7" y="9" width="12" height="8.5" fill="var(--sand)"/>
        <path d="M7,9 L13,14 L19,9" fill="none" stroke="var(--white)" stroke-width="1.2"/>
      </svg>accounting@torvelinc.com
    </li>
  </ul>
  <p class="back__services">AIR, OCEAN, FTL, LTL, EXPRESS</p>
  <div class="back__badge">
    <div class="back__badge-name">TORVEL</div>
  </div>
  <svg class="card__wave" viewBox="0 0 650 371" aria-hidden="true">
    <path fill="var(--white)" d="M0,308 C120,290 250,285 330,330 C420,375 560,330 650,292 L650,371 L0,371 Z"/>
    <path fill="var(--charcoal)" d="M0,332 C130,312 250,315 330,350 C420,385 560,355 650,318 L650,371 L0,371 Z"/>
  </svg>
</section>

</body>
</html>
```